Certificates with Watermark Images

We are looking for a design of One page Certificates with Watermark (background) images where text will be printed over it .
Graphics design is required to reflect the flowing categories:
IPTV (Internet Protocol TV)
VoD (Video on Demand)
Satellite Receiver
Graphics design images for all three categories must be provided to maintain the same them .
Thank you and good luck.
Internet
- Graphics design images for all three categories must be provided to maintain the same them

```html
<!DOCTYPE html>
<html lang="en">
<head>
<meta charset="UTF-8">
<title>Certificate Series – IPTV, VoD, Satellite Receiver</title>
<link rel="stylesheet" href="https://fonts.googleapis.com/css2?family=Cinzel:wght@400;600;700&display=swap">
<style>
  :root {
    --canvas-bg: #ffffff;
    --paper: #f7f2e6;
    --panel: #fdfbf4;
    --border-deep: #4f6fc4;
    --border-mid: #7f9ad8;
    --border-light: #b9c8ec;
    --title-ink: #a08c7c;
    --title-shade: #5e4c40;
    --title-light: #f4ece4;
  }

  * { box-sizing: border-box; margin: 0; padding: 0; }

  html, body {
    width: 1200px;
    height: 900px;
    overflow: hidden;
    background: var(--canvas-bg);
  }

  .stage {
    position: relative;
    width: 1200px;
    height: 900px;
  }

  .certificate {
    position: absolute;
    background: var(--paper);
    box-shadow: 0 2px 6px rgba(0, 0, 0, 0.12);
  }

  .certificate__border {
    position: absolute;
    inset: 7px;
    background:
      repeating-linear-gradient(45deg, rgba(255,255,255,0.18) 0 3px, transparent 3px 7px),
      radial-gradient(circle at center, var(--border-light) 0%, var(--border-mid) 55%, var(--border-deep) 100%);
  }

  .certificate__panel {
    position: absolute;
    background: var(--panel);
    box-shadow: 0 0 0 3px var(--border-light), 0 0 0 5px var(--border-mid);
    display: flex;
    flex-direction: column;
    align-items: center;
    justify-content: center;
    text-align: center;
    font-family: "Cinzel", serif;
    color: var(--title-ink);
  }

  .certificate__title {
    font-weight: 700;
    line-height: 1;
    text-shadow:
      -1px -1px 0 var(--title-light),
      2px 2px 0 var(--title-shade),
      3px 4px 4px rgba(0, 0, 0, 0.35);
  }

  .certificate__subtitle {
    font-weight: 600;
    letter-spacing: 0.02em;
    text-shadow: 1px 1px 0 var(--title-shade);
  }

  /* IPTV */
  .certificate--iptv {
    left: 30px; top: 57px;
    width: 420px; height: 326px;
    transform: rotate(-15deg);
    z-index: 1;
  }
  .certificate--iptv .certificate__panel { inset: 58px 56px; }
  .certificate--iptv .certificate__title { font-size: 104px; margin-top: 10px; }
  .certificate--iptv .certificate__subtitle { font-size: 15px; margin-top: 34px; }

  /* VoD */
  .certificate--vod {
    left: 322px; top: 246px;
    width: 500px; height: 382px;
    transform: rotate(-8.5deg);
    z-index: 2;
  }
  .certificate--vod .certificate__panel { inset: 62px 60px; }
  .certificate--vod .certificate__title { font-size: 112px; margin-top: 30px; }
  .certificate--vod .certificate__subtitle { font-size: 17px; margin-top: 42px; }

  /* Satellite Receiver */
  .certificate--satellite {
    left: 691px; top: 482px;
    width: 460px; height: 380px;
    transform: rotate(-4deg);
    z-index: 3;
  }
  .certificate--satellite .certificate__panel { inset: 62px 58px; }
  .certificate--satellite .certificate__title {
    font-size: 42px;
    line-height: 1.15;
    text-shadow:
      -1px -1px 0 var(--title-light),
      1px 2px 0 var(--title-shade),
      2px 3px 3px rgba(0, 0, 0, 0.3);
  }
</style>
</head>
<body>
  <main class="stage">
    <section class="certificate certificate--iptv">
      <div class="certificate__border" role="img" aria-label="Ornamental blue guilloché certificate border"></div>
      <div class="certificate__panel">
        <h2 class="certificate__title">IPTV</h2>
        <p class="certificate__subtitle">(Internat Protocol TV)</p>
      </div>
    </section>

    <section class="certificate certificate--vod">
      <div class="certificate__border" role="img" aria-label="Ornamental blue guilloché certificate border"></div>
      <div class="certificate__panel">
        <h2 class="certificate__title">VoD</h2>
        <p class="certificate__subtitle">(Video on Demand)</p>
      </div>
    </section>

    <section class="certificate certificate--satellite">
      <div class="certificate__border" role="img" aria-label="Ornamental blue guilloché certificate border"></div>
      <div class="certificate__panel">
        <h2 class="certificate__title">Satellite<br>Receiver</h2>
      </div>
    </section>
  </main>
</body>
</html>
```